Business Cards for Corvantis LLC

We need business cards for a new company called “Corvantis LLC”. This is a technology process improvement company providing a comprehensive assessment of the technology used to run their business. The documentation and review process delivers the visibility and reassurance they need to protect their business and plan for the future. The product is called “Halvorne Ledgerwork”. Our primary target is small-medium size businesses, with the deliverables going to the decision maker. We would like to see the designs use the color blue. Our tag line is PROTECT YOUR BUSINESS · TAKE CONTROL OF IT.

Industry/Entity Type

Business

Contact Information for Business Card

Tag line should be on back of card - it does not have to be upper case.

Requirements
Must have
• Please use information when laying out card:
• Name: Darnell Pruitt
• Title: Partner
• Phone Number: (877)555-0143
• Email: dell@corvantisllc.com
• Website: http://corvantisllc.com

```html
<!DOCTYPE html>
<html lang="en">
<head>
<meta charset="utf-8">
<title>Corvantis LLC – Business Card</title>
<link rel="stylesheet" href="https://fonts.googleapis.com/css2?family=Open+Sans:wght@400;600;700&display=swap">
<style>
  :root {
    --page-bg: #e9edf2;
    --card-top: #f6f8fa;
    --card-bottom: #e4e9ef;
    --brand-blue: #0d4c9e;
    --brand-blue-deep: #0a3f86;
    --swoosh-grey: #6e7378;
    --text-grey: #55595e;
    --web-grey: #c9d2e0;
  }
  html, body {
    margin: 0;
    padding: 0;
    width: 1200px;
    height: 970px;
    overflow: hidden;
    background: var(--page-bg);
    font-family: "Open Sans", Arial, sans-serif;
  }
  .business-card {
    position: absolute;
    left: 100px;
    top: 201px;
    width: 1000px;
    height: 568px;
    border-radius: 22px;
    overflow: hidden;
    background: linear-gradient(180deg, var(--card-top), var(--card-bottom));
    box-shadow: 0 14px 36px rgba(20, 40, 70, 0.18);
  }
  .card-art {
    position: absolute;
    inset: 0;
    width: 1000px;
    height: 568px;
  }
  .name-marker {
    position: absolute;
    left: -30px;
    top: 58px;
    width: 60px;
    height: 60px;
    border-radius: 50%;
    background: var(--brand-blue);
  }
  .person {
    position: absolute;
    left: 57px;
    top: 58px;
  }
  .person-name {
    margin: 0;
    color: var(--brand-blue);
    font-size: 35px;
    font-weight: 700;
    line-height: 38px;
  }
  .person-title {
    margin: 0;
    color: var(--text-grey);
    font-size: 26px;
    font-weight: 400;
    line-height: 26px;
  }
  .contact-list {
    position: absolute;
    left: 57px;
    top: 214px;
    margin: 0;
    padding: 0;
    list-style: none;
  }
  .contact-item {
    display: flex;
    align-items: center;
    height: 38px;
    color: var(--text-grey);
    font-size: 27px;
  }
  .contact-icon {
    width: 30px;
    height: 30px;
    margin-right: 12px;
    flex: none;
  }
  .tagline {
    position: absolute;
    left: 57px;
    top: 333px;
    margin: 0;
    color: var(--brand-blue);
    font-size: 25px;
    font-weight: 600;
    letter-spacing: 0.6px;
    line-height: 32px;
    text-transform: uppercase;
  }
  .brand {
    position: absolute;
    left: 541px;
    top: 198px;
    width: 400px;
    display: flex;
    align-items: center;
    justify-content: center;
    gap: 14px;
  }
  .brand-square {
    width: 34px;
    height: 34px;
    background: var(--brand-blue);
  }
  .brand-name {
    color: var(--brand-blue);
    font-size: 50px;
    font-weight: 700;
    line-height: 60px;
    white-space: nowrap;
  }
  .website {
    position: absolute;
    left: 740px;
    top: 484px;
    color: var(--web-grey);
    font-size: 26px;
    font-weight: 400;
  }
</style>
</head>
<body>
  <div class="business-card">
    <svg class="card-art" viewBox="0 0 1000 568" aria-hidden="true">
      <path class="swoosh" d="M0 396 C 150 470, 300 520, 470 512 C 560 508, 620 480, 650 460 C 590 495, 520 508, 450 504 C 290 496, 140 450, 0 420 Z" fill="var(--swoosh-grey)"/>
      <path class="wave-band" d="M0 434 C 120 480, 240 512, 360 512 C 520 512, 650 440, 800 410 C 870 398, 940 396, 1000 398 L 1000 568 L 0 568 Z" fill="var(--brand-blue)"/>
    </svg>

    <div class="name-marker"></div>

    <div class="person">
      <p class="person-name">Darnell Pruitt</p>
      <p class="person-title">Partner</p>
    </div>

    <ul class="contact-list">
      <li class="contact-item">
        <svg class="contact-icon" viewBox="0 0 30 30" aria-hidden="true">
          <rect width="30" height="30" rx="4" fill="var(--brand-blue)"/>
          <path d="M10 7 C 8 8, 8 10, 9 13 C 10.5 17, 13 20.5, 17 22.5 C 19.5 23.5, 21 23, 22 21 L 19.5 18.5 L 17.5 19.5 C 15 18, 13 15.5, 12 13 L 13.5 11 Z" fill="#fff"/>
        </svg>
        (877)555-0143
      </li>
      <li class="contact-item">
        <svg class="contact-icon" viewBox="0 0 30 30" aria-hidden="true">
          <rect width="30" height="30" rx="4" fill="var(--brand-blue)"/>
          <rect x="6" y="9" width="18" height="13" fill="none" stroke="#fff" stroke-width="1.8"/>
          <path d="M6 9 L15 16.5 L24 9 M6 22 L12.5 15 M24 22 L17.5 15" fill="none" stroke="#fff" stroke-width="1.6"/>
        </svg>
        dell@corvantisllc.com
      </li>
    </ul>

    <p class="tagline">Protect your business<br>Take control of IT.</p>

    <div class="brand">
      <span class="brand-square"></span>
      <span class="brand-name">Corvantis LLC</span>
    </div>

    <span class="website">corvantisllc.com</span>
  </div>
</body>
</html>
```